Wordpress Design ProjectWP website design (Vosberg)

We need a wordpress design that will incorporate a professional color scheme with company logo in a clean layout. The design needs to consider that this will be developed on a responsive theme. Colors are undetermined - use a colors in logo - maybe a light color, maybe yellow accent, and black. Client wants a 'modern' look.

Industry/Entity Type

It Company

Font styles to use
Serif
Sans Serif

Requirements
Must have
• Navigation: 1) Home 2) Auctions 3) Services 4) About Us 5) Contact us
• Site will have a slideshow element (initial image attached) and the following widgets: 1)Social Media (facebook,RSS) 2) Email Sign Up Form 3) Featured Video, 4) Auction Search
• Homepage content: "Vosberg Auction & Real Estate
• Since 1958 We at Vosberg Auction & Real Estate have offered our services to our clients as a versatile Auction Company with the ability to perform a variety of Auction types.
• Having sold Items such as: Real Estate, Machinery, Antiques, Tools, and much, more; we have constructed a strong foundation of knowledge and experience of the appropriate Auction marketing and preparation logistics. This results in a high quality Auction service that we provide to our clients, and also a level of service that we take great pride in.
• When you are ready for your Auction, you want it done right!
• Call Us at Vosberg Auction & Real Estate,"
• In the footer, there will be smaller company logo, the affiliations logo (attached), and contact info below:
• Vosberg Auction, Inc.
• 4135 County Highway 82
• Harlow Falls, NY 13921
• 607-555-0143
Nice to have
• Use of a dropdown menu with styling.

```html
<!DOCTYPE html>
<html lang="en">
<head>
<meta charset="utf-8">
<title>Vosberg Auction</title>
<link rel="stylesheet" href="https://fonts.googleapis.com/css2?family=Tinos:wght@400;700&family=Arimo:wght@400;700&family=Ubuntu:wght@400;500&display=swap">
<style>
:root{
  --navy:#1f1f5e;
  --royal:#1f2080;
  --ink:#111;
  --text:#222;
  --light:#efefef;
  --field:#f2f2f2;
  --footer:#262626;
  --white:#fff;
  --fb:#0c4a7a;
  --rss:#f0920e;
}
*{box-sizing:border-box;margin:0;padding:0}
html,body{width:1075px;height:1200px;overflow:hidden;background:var(--white)}
body{position:relative;font-family:"Arimo",Arial,sans-serif;color:var(--text)}
.abs{position:absolute}
h1,h2{font-weight:400}

/* header */
.site-header{left:0;top:0;width:1075px;height:118px;background:var(--white)}
.brand{left:94px;top:36px;display:flex;align-items:center;gap:10px}
.brand-mark{width:30px;height:30px;border-radius:50%;background:var(--navy)}
.brand-name{font-family:"Tinos",serif;font-weight:700;font-size:38px;color:var(--navy);letter-spacing:1px}
.follow{left:796px;top:47px;font-family:"Tinos",serif;font-size:20px;color:var(--ink)}
.social{top:42px;width:34px;height:34px;border-radius:50%}
.social.fb{left:899px;background:var(--fb)}
.social.rss{left:948px;background:var(--rss)}

/* nav */
.main-nav{left:0;top:118px;width:1075px;height:40px;background:var(--navy)}
.nav-item{top:0;height:40px;line-height:40px;font-family:"Tinos",serif;font-size:17px;color:var(--white)}
.nav-item.active{top:5px;height:29px;line-height:29px;left:105px;width:86px;text-align:center;background:var(--light);color:#333}
.nav-divider{top:0;width:1px;height:40px;background:#34347a}

/* hero */
.hero{left:0;top:158px;width:1075px;height:408px;background:linear-gradient(180deg,#4f7a2f 0%,#6b5146 35%,#8a4a38 60%,#4c7a2c 100%)}
.search-panel{left:684px;top:290px;width:302px;height:230px;background:rgba(25,25,25,.85)}
.search-title{left:709px;top:309px;font-family:"Tinos",serif;font-size:28px;color:var(--white)}
.field{background:var(--field);border-radius:16px;font-size:14px;color:#666;padding-left:17px;display:flex;align-items:center}
.search-input{left:709px;top:362px;width:243px;height:31px}
.search-select{left:709px;top:411px;width:243px;height:31px}
.caret{position:absolute;right:14px;top:13px}
.btn-subscribe-now{left:817px;top:462px;width:135px;height:36px;border-radius:9px;background:var(--royal);border:1px solid #5a6fd0;color:var(--white);font-family:"Ubuntu",sans-serif;font-size:16px;display:flex;align-items:center;justify-content:center}

/* welcome */
.welcome-title{left:0;top:605px;width:1075px;text-align:center;font-family:"Tinos",serif;font-weight:700;font-size:23px;color:var(--ink)}
.welcome-title .accent{color:var(--navy)}
.welcome-text{left:128px;top:647px;width:819px;text-align:center;font-size:12px;line-height:19.7px;color:var(--text)}

/* features */
.features{left:0;top:758px;width:1075px;height:285px;background:var(--light)}
.video-thumb{left:90px;top:796px;width:255px;height:173px;background:linear-gradient(180deg,#4d8fd8 0%,#9ec3e8 45%,#4f8a36 75%,#3c7a22 100%)}
.play{left:188px;top:853px}
.feature-title{left:368px;top:794px;font-family:"Tinos",serif;font-weight:400;font-size:23px;color:var(--ink);letter-spacing:.5px}
.feature-text{left:370px;top:829px;width:277px;font-size:12px;line-height:18.8px;text-align:justify}
.btn-learn{left:371px;top:938px;width:85px;height:23px;border-radius:3px;background:var(--royal);color:var(--white);font-size:12px;display:flex;align-items:center;justify-content:center}
.signup{left:710px;top:785px;width:263px;height:222px;background:var(--royal);border-radius:3px}
.signup-title{left:728px;top:795px;font-family:"Tinos",serif;font-weight:400;font-size:27px;color:var(--white)}
.signup-text{left:729px;top:834px;width:230px;font-size:11px;line-height:14px;color:var(--white);text-align:justify;font-weight:700}
.input{width:221px;height:27px;background:#f7f7f7;border:1px solid #ccc;font-size:12px;color:#777;padding-left:7px;display:flex;align-items:center}
.input.name{left:729px;top:878px}
.input.email{left:729px;top:924px}
.btn-subscribe{left:729px;top:961px;width:93px;height:28px;border-radius:3px;background:#000;border:1px solid #444;color:var(--white);font-family:"Ubuntu",sans-serif;font-size:14px;display:flex;align-items:center;justify-content:center;letter-spacing:.5px}

/* footer */
.site-footer{left:0;top:1043px;width:1075px;height:129px;background:var(--footer)}
.address{left:105px;top:1070px;font-size:13px;line-height:19.7px;color:var(--white);font-style:normal}
.foot-link{top:1061px;font-family:"Tinos",serif;font-weight:700;font-size:13px;color:var(--white)}
.foot-brand{left:694px;top:1110px;font-family:"Tinos",serif;font-weight:700;font-size:24px;color:var(--white)}
.badge-circle{left:822px;top:1097px;width:92px;height:62px;border-radius:50%;background:var(--white)}
.badge-square{left:930px;top:1100px;width:47px;height:53px;background:var(--white)}
.copyright{left:0;top:1172px;width:1075px;height:28px;background:var(--navy);color:var(--white);font-size:11px;display:flex;align-items:center;justify-content:center}
</style>
</head>
<body>

<header class="site-header abs">
  <div class="brand abs"><span class="brand-mark"></span><span class="brand-name">VOSBERG</span></div>
  <div class="follow abs">Follow Us:</div>
  <span class="social fb abs" aria-label="Social profile"></span>
  <span class="social rss abs" aria-label="News feed"></span>
</header>

<nav class="main-nav abs">
  <span class="nav-item active abs">Home</span>
  <span class="nav-divider abs" style="left:202px"></span>
  <span class="nav-item abs" style="left:237px">Auctions</span>
  <span class="nav-divider abs" style="left:335px"></span>
  <span class="nav-item abs" style="left:369px">Services</span>
  <span class="nav-divider abs" style="left:462px"></span>
  <span class="nav-item abs" style="left:498px">About Us</span>
  <span class="nav-divider abs" style="left:599px"></span>
  <span class="nav-item abs" style="left:634px">Contact us</span>
</nav>

<section class="hero abs" role="img" aria-label="Slideshow photo of a red brick house with a gabled roof surrounded by trees and flowering shrubs"></section>
<div class="search-panel abs"></div>
<div class="search-title abs">Auction Search</div>
<div class="field search-input abs">Search...</div>
<div class="field search-select abs">All Catagories
  <svg class="caret" width="16" height="8" viewBox="0 0 16 8"><path d="M0 0h16L8 8z" fill="#333"/></svg>
</div>
<div class="btn-subscribe-now abs">Subscribe Now</div>

<h1 class="welcome-title abs"><span class="accent">WELCOME</span> VOSBERG AUCTION</h1>
<p class="welcome-text abs">Lorem ipsum dolor sit amet, consectetur adipiscing elit, sed do eiusmod tempor incididunt ut labore et dolore magna aliqua. Ut enim ad minim veniam, quis nostrud exercitation ullamco laboris nisi ut aliquip ex ea commodo consequat. Duis aute irure dolor in reprehenderit in voluptate velit esse cillum dolore eu fugiat nulla pariatur. Excepteur sint occaecat cupidatat non proident, sunt in culpa qui officia deserunt mollit anim id est laborum. Sed ut perspiciatis unde omnis iste natus error sit voluptatem accusantium</p>

<section class="features abs"></section>
<div class="video-thumb abs" role="img" aria-label="Featured video still of an agent in a suit standing on a lawn in front of a house"></div>
<svg class="play abs" width="58" height="58" viewBox="0 0 58 58" aria-hidden="true">
  <circle cx="29" cy="29" r="26" fill="rgba(0,0,0,.35)" stroke="rgba(255,255,255,.8)" stroke-width="4"/>
  <path d="M22 17l18 12-18 12z" fill="rgba(255,255,255,.8)"/>
</svg>
<h2 class="feature-title abs">Feature Video</h2>
<p class="feature-text abs">Lorem ipsum dolor sit amet, consectetur adipiscing elit, sed do eiusmod tempor incididunt ut labore et dolore magna aliqua. Ut enim ad minim veniam, quis nostrud exercitation ullamco laboris nisi ut aliquip ex ea commodo consequat.</p>
<div class="btn-learn abs">Learn More</div>

<div class="signup abs"></div>
<h2 class="signup-title abs">Email Sign Up</h2>
<p class="signup-text abs">Lorem ipsum dolor sit amet, consectetuer adipiscing elit. Nam</p>
<div class="input name abs">Your Name</div>
<div class="input email abs">Email Address</div>
<div class="btn-subscribe abs">Subscribe</div>

<footer class="site-footer abs"></footer>
<address class="address abs">Vosberg Auction, Inc.<br>4135 County Highway 82<br>Harlow Falls, NY 13921<br>607-555-0143</address>
<span class="foot-link abs" style="left:531px">Home</span>
<span class="foot-link abs" style="left:617px">Auctions</span>
<span class="foot-link abs" style="left:719px">Services</span>
<span class="foot-link abs" style="left:820px">About Us</span>
<span class="foot-link abs" style="left:926px">Contact us</span>
<div class="foot-brand abs">VOSBERG</div>
<span class="badge-circle abs" aria-label="Affiliation badge"></span>
<span class="badge-square abs" aria-label="Affiliation badge"></span>
<div class="copyright abs">Copyright (C) Vosberg auction. 2014.&nbsp; All Rights Reserved</div>

</body>
</html>
```